Create a business promotion flyer to leave in customer mailboxes. We are a bulk petroleum supplier, servicing any industry that requires diesel. Base in Brindlemere Valley, servicing griffith area and surrounds.

Business Name - Terra Petro
Fuel@terrapetro-example.com.au
Marco - 0400 000 001 mtorrisi@terrapetro-example.com.au
Liam - 0400 000 002 lharcourt@terrapetro-example.com.au
Peter - 0400 000 003 pwinslow@terrapetro-example.com.au
Office 02 5550 0100

Bulk Fuel deliveries.
Oils & lubricants
Local Family owned business

```html
<!DOCTYPE html>
<html lang="en">
<head>
<meta charset="utf-8">
<title>Terra Petro – Mailbox Flyer</title>
<link rel="stylesheet" href="https://fonts.googleapis.com/css2?family=Raleway:wght@500;600;700&family=Oswald:wght@400&family=Allura&family=Roboto+Condensed:wght@400;700&display=swap">
<style>
  :root {
    --red: #e4271f;
    --slate: #5a6063;
    --ink: #3b4043;
    --paper: #ffffff;
    --sky-top: #ffffff;
    --sky: #a9c6e6;
    --shed: #9aa2a8;
  }
  * { box-sizing: border-box; margin: 0; padding: 0; }
  html, body { width: 848px; height: 1200px; overflow: hidden; background: var(--paper); }
  .flyer { position: relative; width: 848px; height: 1200px; background: var(--paper); font-family: "Raleway", sans-serif; }

  .brand { position: absolute; top: 70px; left: 0; width: 100%; display: flex; justify-content: center; align-items: center; gap: 14px; z-index: 2; }
  .brand-dot { width: 34px; height: 34px; border-radius: 50%; background: var(--red); }
  .brand-name { font-weight: 600; font-size: 56px; color: var(--ink); letter-spacing: 0.5px; }

  .hero { position: absolute; top: 150px; left: 0; width: 100%; height: 340px;
    background: linear-gradient(180deg, var(--sky-top) 0%, var(--sky) 38%, #c8d4de 58%, var(--shed) 78%, #6d7378 100%); }

  .headline { position: absolute; top: 488px; left: 0; width: 100%; height: 152px; background: var(--red); color: #fff; padding: 32px 0 0 46px; }
  .headline h1 { font-weight: 600; font-size: 33px; letter-spacing: 0.3px; }
  .headline .tagline { font-family: "Allura", cursive; font-size: 52px; line-height: 1; }

  .services { position: absolute; top: 640px; left: 0; width: 100%; height: 175px; display: flex; justify-content: space-between; align-items: center; padding: 0 30px; }
  .service { display: flex; align-items: center; gap: 14px; }
  .service-icon { width: 66px; height: 66px; border-radius: 50%; background: var(--red); display: flex; align-items: center; justify-content: center; }
  .service-label { font-family: "Oswald", sans-serif; font-size: 25px; line-height: 1.2; color: var(--ink); text-transform: uppercase; }

  .industry { position: absolute; top: 815px; left: 0; width: 100%; height: 137px; background: var(--slate); color: #fff; text-align: center; padding-top: 30px; }
  .industry p { font-weight: 600; font-size: 31px; line-height: 1.15; letter-spacing: 0.3px; }
  .industry .underline { display: inline-block; border-bottom: 4px solid var(--red); }

  .contacts { position: absolute; top: 952px; left: 0; width: 100%; height: 136px; display: flex; align-items: center; padding: 0 14px 0 20px; }
  .contact { flex: 1; min-width: 0; border-left: 2px solid var(--ink); padding: 2px 0 2px 7px; font-family: "Roboto Condensed", sans-serif; }
  .contact:first-child { border-left: none; padding-left: 0; }
  .contact h3 { font-size: 17px; font-weight: 700; color: var(--red); margin-bottom: 3px; }
  .contact .line { display: flex; align-items: center; gap: 4px; font-size: 11px; color: var(--ink); white-space: nowrap; line-height: 1.45; letter-spacing: -0.2px; }
  .contact svg { flex: none; }

  .footer { position: absolute; top: 1088px; left: 0; width: 100%; height: 112px; background: var(--red); color: #fff; text-align: center; padding-top: 24px; font-family: "Roboto Condensed", sans-serif; }
  .footer p { font-size: 28px; line-height: 1.25; }
  .footer em { font-style: italic; font-weight: 700; font-size: 26px; }
</style>
</head>
<body>
<main class="flyer">
  <header class="brand">
    <span class="brand-dot"></span>
    <span class="brand-name">Terra Petro</span>
  </header>

  <div class="hero" role="img" aria-label="Photo of a white double tanker fuel truck parked in front of a steel shed under a blue cloudy sky"></div>

  <section class="headline">
    <h1>FUELING YOUR BUSINESS.</h1>
    <p class="tagline">Keeping your industry moving.</p>
  </section>

  <section class="services">
    <div class="service">
      <span class="service-icon">
        <svg width="38" height="38" viewBox="0 0 40 40" fill="none" stroke="#fff" stroke-width="3" stroke-linecap="round" stroke-linejoin="round">
          <path d="M8 32 L20 20 L26 26 L14 38"/>
          <path d="M20 20 L30 10 L34 14 L26 22"/>
          <path d="M30 10 L36 4"/>
        </svg>
      </span>
      <span class="service-label">Bulk Fuel<br>Deliveries</span>
    </div>
    <div class="service">
      <span class="service-icon">
        <svg width="40" height="40" viewBox="0 0 40 40">
          <g fill="#fff">
            <circle cx="20" cy="20" r="12"/>
            <rect x="17" y="3" width="6" height="8" rx="1"/>
            <rect x="17" y="29" width="6" height="8" rx="1"/>
            <rect x="3" y="17" width="8" height="6" rx="1"/>
            <rect x="29" y="17" width="8" height="6" rx="1"/>
            <rect x="17" y="3" width="6" height="8" rx="1" transform="rotate(45 20 20)"/>
            <rect x="17" y="3" width="6" height="8" rx="1" transform="rotate(135 20 20)"/>
            <rect x="17" y="3" width="6" height="8" rx="1" transform="rotate(225 20 20)"/>
            <rect x="17" y="3" width="6" height="8" rx="1" transform="rotate(315 20 20)"/>
          </g>
          <path d="M20 13 C17 17 16 19 16 21 a4 4 0 0 0 8 0 C24 19 23 17 20 13 Z" fill="#e4271f"/>
        </svg>
      </span>
      <span class="service-label">Oils<br>&amp; Lubricants</span>
    </div>
    <div class="service">
      <span class="service-icon">
        <svg width="42" height="42" viewBox="0 0 42 42" fill="none" stroke="#fff" stroke-width="2.6">
          <circle cx="21" cy="14" r="5"/>
          <path d="M12 31 a9 9 0 0 1 18 0 Z"/>
          <circle cx="10" cy="17" r="4"/>
          <path d="M3 30 a7 7 0 0 1 9 -7"/>
          <circle cx="32" cy="17" r="4"/>
          <path d="M39 30 a7 7 0 0 0 -9 -7"/>
        </svg>
      </span>
      <span class="service-label">Local Family<br>Owned Business</span>
    </div>
  </section>

  <section class="industry">
    <p>SERVICING ANY INDUSTRY</p>
    <p><span class="underline">THAT REQUIRES DIESEL</span></p>
  </section>

  <section class="contacts">
    <div class="contact">
      <h3>Office</h3>
      <p class="line"><svg width="11" height="11" viewBox="0 0 12 12"><circle cx="6" cy="6" r="6" fill="#e4271f"/><path d="M4 3 L5 5 L4.5 6 Q5.5 7.5 6 7.5 L7 7 L9 8 Q8 10 6 9 Q3 7.5 3 4 Z" fill="#fff"/></svg>02 5550 0100</p>
      <p class="line"><svg width="11" height="11" viewBox="0 0 12 12"><circle cx="6" cy="6" r="6" fill="#e4271f"/><rect x="3" y="4" width="6" height="4" fill="#fff"/></svg>Fuel@terrapetro-example.com.au</p>
    </div>
    <div class="contact">
      <h3>Marco</h3>
      <p class="line"><svg width="11" height="11" viewBox="0 0 12 12"><circle cx="6" cy="6" r="6" fill="#e4271f"/><path d="M4 3 L5 5 L4.5 6 Q5.5 7.5 6 7.5 L7 7 L9 8 Q8 10 6 9 Q3 7.5 3 4 Z" fill="#fff"/></svg>0400 000 001</p>
      <p class="line"><svg width="11" height="11" viewBox="0 0 12 12"><circle cx="6" cy="6" r="6" fill="#e4271f"/><rect x="3" y="4" width="6" height="4" fill="#fff"/></svg>mtorrisi@terrapetro-example.com.au</p>
    </div>
    <div class="contact">
      <h3>Liam</h3>
      <p class="line"><svg width="11" height="11" viewBox="0 0 12 12"><circle cx="6" cy="6" r="6" fill="#e4271f"/><path d="M4 3 L5 5 L4.5 6 Q5.5 7.5 6 7.5 L7 7 L9 8 Q8 10 6 9 Q3 7.5 3 4 Z" fill="#fff"/></svg>0400 000 002</p>
      <p class="line"><svg width="11" height="11" viewBox="0 0 12 12"><circle cx="6" cy="6" r="6" fill="#e4271f"/><rect x="3" y="4" width="6" height="4" fill="#fff"/></svg>lharcourt@terrapetro-example.com.au</p>
    </div>
    <div class="contact">
      <h3>Peter</h3>
      <p class="line"><svg width="11" height="11" viewBox="0 0 12 12"><circle cx="6" cy="6" r="6" fill="#e4271f"/><path d="M4 3 L5 5 L4.5 6 Q5.5 7.5 6 7.5 L7 7 L9 8 Q8 10 6 9 Q3 7.5 3 4 Z" fill="#fff"/></svg>0400 000 003</p>
      <p class="line"><svg width="11" height="11" viewBox="0 0 12 12"><circle cx="6" cy="6" r="6" fill="#e4271f"/><rect x="3" y="4" width="6" height="4" fill="#fff"/></svg>pwinslow@terrapetro-example.com.au</p>
    </div>
  </section>

  <footer class="footer">
    <p>Your local bulk petroleum supplier</p>
    <p><em>Brindlemere Valley and surrounds</em></p>
  </footer>
</main>
</body>
</html>
```